A clean crisp business card for a Landscape Construction company. Designed to be easy to read contact/ info and also be appealing/interesting, unlike a traditional business card.

Industry/Entity Type

Landscape Construction

Contact Information for Business Card

Company name : Bramblecrest Landscape Construction, phone number: (877) 62Vales, website:Bramblecrestlandscapes.example, Email, sales@bramblecrestlandscapes.example

Requirements
Nice to have
• Luxurious finishes/ details…. Icons or emblems next to contact info
Should not have
• Clipart or general pictures

```html
<!DOCTYPE html>
<html lang="en">
<head>
<meta charset="utf-8">
<title>Bramblecrest Landscape Construction – Business Card</title>
<link href="https://fonts.googleapis.com/css2?family=Montserrat:wght@400;500;600;800&display=swap" rel="stylesheet">
<style>
  :root {
    --page-bg: #eef2f5;
    --card-white: #ffffff;
    --brand-blue: #1f6bb5;
    --deep-blue: #17528e;
    --mid-blue: #2a78c2;
    --leaf-green: #8cc540;
    --ink: #2c2c2c;
    --radius: 22px;
  }
  * { margin: 0; padding: 0; box-sizing: border-box; }
  html, body {
    width: 1200px; height: 1027px; overflow: hidden;
    background: var(--page-bg);
    font-family: "Montserrat", Arial, sans-serif;
  }
  .canvas { position: relative; width: 1200px; height: 1027px; }
  .card {
    position: absolute; left: 250px; width: 700px; height: 400px;
    border-radius: var(--radius); overflow: hidden;
    box-shadow: 0 10px 30px rgba(20, 50, 90, 0.15);
  }
  .card-front { top: 83px; background: var(--card-white); }
  .card-back {
    top: 543px;
    background: linear-gradient(135deg, #5d9bd4 0%, var(--brand-blue) 45%, var(--deep-blue) 100%);
    display: flex; align-items: center; justify-content: center; gap: 18px;
  }
  .side-band {
    position: absolute; top: 0; right: 0; width: 150px; height: 100%;
    background: linear-gradient(180deg, var(--mid-blue) 0%, var(--deep-blue) 100%);
  }
  .side-rule {
    position: absolute; top: 0; right: 162px; width: 6px; height: 100%;
    background: var(--leaf-green);
  }
  .brand {
    position: absolute; left: 60px; top: 70px;
    display: flex; align-items: center; gap: 14px;
  }
  .brand-dot { width: 38px; height: 38px; border-radius: 50%; background: var(--leaf-green); }
  .brand-name {
    font-weight: 600; font-size: 25px; line-height: 1.2; color: var(--brand-blue);
    width: 270px;
  }
  .person { position: absolute; left: 60px; top: 190px; }
  .person-name { font-weight: 800; font-size: 26px; color: var(--brand-blue); }
  .person-title { font-weight: 400; font-size: 19px; color: var(--ink); margin-top: 4px; }
  .contact-list { position: absolute; left: 60px; top: 285px; list-style: none; }
  .contact-item {
    display: flex; align-items: center; gap: 14px;
    font-size: 17px; color: var(--ink); height: 30px;
  }
  .contact-icon { width: 20px; height: 20px; flex: none; }
  .back-dot { width: 46px; height: 46px; border-radius: 50%; background: var(--leaf-green); }
  .back-name {
    font-weight: 600; font-size: 34px; color: var(--card-white); line-height: 1.15;
    width: 360px;
  }
</style>
</head>
<body>
<main class="canvas">

  <section class="card card-front" aria-label="Business card front">
    <div class="side-rule" aria-hidden="true"></div>
    <div class="side-band" aria-hidden="true"></div>

    <div class="brand">
      <span class="brand-dot"></span>
      <span class="brand-name">Bramblecrest Landscape Construction</span>
    </div>

    <div class="person">
      <p class="person-name">Marcus Ellery</p>
      <p class="person-title">Managing Partner</p>
    </div>

    <ul class="contact-list">
      <li class="contact-item">
        <svg class="contact-icon" viewBox="0 0 24 24" aria-hidden="true"><path d="M6.6 10.8a15 15 0 0 0 6.6 6.6l2.2-2.2a1 1 0 0 1 1-.25 11.4 11.4 0 0 0 3.6.57 1 1 0 0 1 1 1V20a1 1 0 0 1-1 1A17 17 0 0 1 3 4a1 1 0 0 1 1-1h3.5a1 1 0 0 1 1 1c0 1.25.2 2.45.57 3.57a1 1 0 0 1-.25 1z" fill="var(--brand-blue)"/></svg>
        <span>(877) 62Vales</span>
      </li>
      <li class="contact-item">
        <svg class="contact-icon" viewBox="0 0 24 24" aria-hidden="true"><rect x="2" y="5" width="20" height="14" rx="1" fill="none" stroke="var(--brand-blue)" stroke-width="1.8"/><path d="M2 6l10 7 10-7" fill="none" stroke="var(--brand-blue)" stroke-width="1.8"/></svg>
        <span>sales@bramblecrestlandscapes.example</span>
      </li>
      <li class="contact-item">
        <svg class="contact-icon" viewBox="0 0 24 24" aria-hidden="true"><g fill="none" stroke="var(--leaf-green)" stroke-width="1.6"><circle cx="12" cy="12" r="10"/><ellipse cx="12" cy="12" rx="4.5" ry="10"/><path d="M2 12h20M4 7h16M4 17h16"/></g></svg>
        <span>www.bramblecrestlandscapes.example</span>
      </li>
    </ul>
  </section>

  <section class="card card-back" aria-label="Business card back">
    <span class="back-dot"></span>
    <span class="back-name">Bramblecrest Landscape Construction</span>
  </section>

</main>
</body>
</html>
```